Stonvale Depot needs a Self-Mailer Brochure Design

NOTE: DO NOT COPY OUR CURRENT BROCHURE DESIGN, WE DON'T LIKE IT AND LOOKING FOR SOMETHING NEW.

I am in charge of marketing at Stonvale Depot. I need create a new self-mailer brochure with our products.

Brief introduction:
• We are wholesaler specializing in home hardware and building supplies. We sell high-end products at better prices.
• Here's some of the items we sell: Bathtub Sales, Faucet Sales, Range Hood
Sales, Shower Sales, Sink Sales, Toilet Sales, Tile Sales, Kitchen supply
sales, Bathroom Supply Sales, Vanities, Lighting, Door Hardware, Mouldings etc.
• Areas Served: Greater Phoenix Area. We are trying to target local businesses in the Phoenix area. Our zip code is 85040.

We would like to create a new self-mailer brochure, that is going to
list our products. The current self-mailer brochure we have is not as organized as we need it to be. We need to make it well-organized and more efficient for our potential customers. I'm attaching our current self-mailer brochure as a reference, Please see the current self-mailer brochure to get an idea of what we need exactly, it will help you to come up with a better concept of putting it all together.

• On the first page, we'd like to include all the essential information about us, and our products- our logo and address, the discounts we provide, and the variety of products that we offer.
• On the other pages, we'd like to list our products with images and descriptions, just like in the current brochure.
• Please make it look appealing to the customer, start the listing with vanities/faucets/surfaces etc.
• You could include the "compare prices" section, just like in current brochure, but only on the first page, instead of every item (Our competitor is Drent, you can find it in the current brochure)
• We're open to suggestions, so please advise on the design (Simple clean lines, high-end, luxury theme would work best)
• Also, it is important to include all the necessary requirements for a self-mailer so we meet the required specification (you can find the requirements online)

Please find all the imagery and descriptions on our website- https://www.stonvaledepot-example.com/ - all the images in high res.
The format is 8/5X11", 2 pages, on both sides.

Please email me at quietlark.mira@mailtrove-example.com, or text me through the platform if you have any questions!
Current brochure and logo are attached,

Looking forward to hear back from you!

Mira

Target Market(s)

Local Businesses in Phoenix

Industry/Entity Type

Building Product

Font styles to use
Serif

Colors
abd036
000000
5c5c5c
ffffff

Requirements
Must have
• We would like to create a new self-mailer brochure, that is going to
• list our products. The current self-mailer brochure we have is not as organized as we need it to be. We need to make it well-organized and more efficient for our potential customers. I'm attaching our current self-mailer brochure as a reference, Please see the current self-mailer brochure to get an idea of what we need exactly, it will help you to come up with a better concept of putting it all together.
• • On the first page, we'd like to include all the essential information about us, and our products- our logo and address, the discounts we provide, and the variety of products that we offer.
• • On the other pages, we'd like to list our products with images and descriptions, just like in the current brochure.
• • Please make it look appealing to the customer, start the listing with vanities/faucets/surfaces etc. by category (check our website to get familiar with categories)
• • You could include the "compare prices" section, just like in current brochure, but only on the first page, instead of every item (Our competitor is Drent, you can find it in the current brochure)
• • We're open to suggestions, so please advise on the design (Simple clean lines, high-end, luxury theme would work best)
• • Also, it is important to include all the necessary requirements for a self-mailer so we meet the required specification (you can find the requirements online)

```html
<!DOCTYPE html>
<html lang="en">
<head>
<meta charset="UTF-8">
<title>Stonvale Depot – Self-Mailer Brochure</title>
<link href="https://fonts.googleapis.com/css2?family=Playfair+Display:wght@400;700&family=Lato:wght@400;700;900&display=swap" rel="stylesheet">
<style>
  :root {
    --lime: #abd036;
    --black: #000000;
    --graphite: #5c5c5c;
    --white: #ffffff;
    --paper: #ffffff;
    --mist: #f3f3f1;
    --rule: #d9d9d6;
    --backdrop: #ececec;
  }
  * { box-sizing: border-box; margin: 0; padding: 0; }
  html, body {
    width: 1200px; height: 960px; overflow: hidden;
    background: var(--backdrop);
    font-family: "Lato", sans-serif;
    color: var(--black);
  }
  .serif { font-family: "Playfair Display", serif; }
  .spread {
    position: absolute; left: 20px; top: 68px;
    width: 1160px; height: 823px; display: flex;
  }
  .page { position: relative; width: 580px; height: 823px; background: var(--paper); overflow: hidden; }
  .page-back { border-right: 1px solid var(--rule); }

  /* ---------- back page: featured products ---------- */
  .section-head { position: absolute; left: 36px; top: 32px; width: 508px; }
  .eyebrow { font-size: 11px; font-weight: 700; letter-spacing: 2.5px; color: var(--graphite); text-transform: uppercase; }
  .section-title { font-family: "Playfair Display", serif; font-weight: 700; font-size: 30px; line-height: 1.15; margin-top: 4px; }
  .section-rule { width: 56px; height: 3px; background: var(--lime); margin-top: 10px; }

  .product-grid { position: absolute; left: 36px; top: 124px; width: 508px; display: flex; gap: 16px; }
  .product-card { width: 158px; }
  .product-photo { width: 158px; height: 150px; }
  .photo-vanity { background: linear-gradient(170deg, #eeeeee 0%, #d8d8d8 50%, #2a2522 51%, #1c1917 100%); }
  .photo-faucet { background: linear-gradient(140deg, #ead3bd 0%, #f3e6d9 45%, #c8c8c8 72%, #8c8c8c 100%); }
  .photo-surface { background: linear-gradient(135deg, #f4f4f2 0%, #dcdcd8 45%, #c9c6c0 70%, #efefec 100%); }
  .product-category { font-size: 10.5px; font-weight: 900; letter-spacing: 2px; color: var(--lime); text-transform: uppercase; margin-top: 12px; }
  .product-name { font-family: "Playfair Display", serif; font-weight: 700; font-size: 16px; line-height: 1.2; margin-top: 4px; }
  .product-desc { font-size: 12px; line-height: 1.45; color: var(--graphite); margin-top: 6px; height: 52px; }
  .product-price { font-size: 13px; font-weight: 700; margin-top: 8px; padding-top: 8px; border-top: 1px solid var(--rule); }

  /* ---------- mailing panel ---------- */
  .mail-panel {
    position: absolute; left: 36px; top: 456px; width: 508px; height: 331px;
    border: 1px solid var(--rule); background: var(--mist);
  }
  .return-address { position: absolute; left: 24px; top: 22px; width: 260px; font-size: 12px; line-height: 1.5; color: var(--graphite); }
  .return-brand { display: flex; align-items: center; gap: 8px; margin-bottom: 4px; }
  .brand-mark { width: 10px; height: 10px; background: var(--lime); flex: none; }
  .return-name { font-family: "Playfair Display", serif; font-weight: 700; font-size: 16px; color: var(--black); }
  .indicia {
    position: absolute; right: 24px; top: 22px; width: 112px; height: 78px;
    border: 1px solid var(--black); text-align: center;
    font-size: 9.5px; font-weight: 700; line-height: 1.35; letter-spacing: 0.5px; padding-top: 7px;
  }
  .addressee { position: absolute; left: 170px; top: 150px; font-size: 13px; line-height: 1.6; letter-spacing: 0.5px; }
  .addressee-code { font-weight: 700; font-size: 12px; }
  .mail-teaser {
    position: absolute; left: 0; bottom: 0; width: 100%; height: 54px;
    background: var(--black); color: var(--white);
    display: flex; align-items: center; justify-content: center; gap: 10px;
    font-family: "Playfair Display", serif; font-size: 17px;
  }
  .mail-teaser strong { color: var(--lime); font-weight: 700; }

  /* ---------- cover page ---------- */
  .masthead { position: absolute; left: 0; top: 0; width: 580px; height: 112px; background: var(--black); color: var(--white); }
  .masthead-brand { position: absolute; left: 36px; top: 30px; display: flex; align-items: center; gap: 12px; }
  .masthead-brand .brand-mark { width: 14px; height: 14px; }
  .brand-name { font-family: "Playfair Display", serif; font-weight: 700; font-size: 30px; color: var(--white); }
  .masthead-tag { position: absolute; left: 62px; top: 74px; font-size: 11px; letter-spacing: 2.5px; color: #bdbdbd; text-transform: uppercase; }
  .masthead-area { position: absolute; right: 36px; top: 40px; text-align: right; font-size: 11px; line-height: 1.5; letter-spacing: 1.5px; color: var(--lime); text-transform: uppercase; font-weight: 700; }

  .hero { position: absolute; left: 0; top: 112px; width: 580px; height: 250px;
    background: linear-gradient(180deg, #eef1f2 0%, #e1e5e7 50%, #b9bcbd 72%, #8f8c87 86%, #c49a70 100%); }
  .offer-badge {
    position: absolute; left: 36px; top: 280px; width: 250px; height: 112px;
    background: var(--lime); color: var(--black); padding: 14px 0 0 20px;
  }
  .offer-lead { font-size: 12px; font-weight: 900; letter-spacing: 2.5px; }
  .offer-value { font-family: "Playfair Display", serif; font-weight: 700; font-size: 38px; line-height: 1.1; margin-top: 2px; }
  .offer-note { font-size: 11px; font-weight: 700; letter-spacing: 1px; margin-top: 4px; }

  .range { position: absolute; left: 36px; top: 416px; width: 508px; }
  .range-title { font-family: "Playfair Display", serif; font-weight: 700; font-size: 20px; }
  .range-list { list-style: none; display: grid; grid-template-columns: repeat(3, 1fr); row-gap: 7px; margin-top: 12px; font-size: 13px; color: var(--graphite); }
  .range-list li { display: flex; align-items: center; gap: 8px; }
  .range-list li::before { content: ""; width: 6px; height: 6px; background: var(--lime); flex: none; }

  .compare { position: absolute; left: 36px; top: 560px; width: 508px; }
  .compare-title { font-family: "Playfair Display", serif; font-weight: 700; font-size: 20px; }
  .compare-table { width: 100%; border-collapse: collapse; margin-top: 10px; font-size: 13px; }
  .compare-table th { text-align: left; font-size: 10.5px; letter-spacing: 1.5px; text-transform: uppercase; color: var(--white); background: var(--graphite); padding: 7px 10px; font-weight: 700; }
  .compare-table td { padding: 7px 10px; border-bottom: 1px solid var(--rule); color: var(--graphite); }
  .compare-table .num { text-align: right; }
  .compare-table .ours { color: var(--black); font-weight: 900; }
  .compare-table th.ours { background: var(--black); color: var(--lime); }

  .cover-footer {
    position: absolute; left: 0; bottom: 0; width: 580px; height: 58px;
    background: var(--black); color: var(--white);
    display: flex; align-items: center; justify-content: space-between; padding: 0 36px;
    font-size: 13px;
  }
  .cover-footer strong { color: var(--lime); font-weight: 700; }
</style>
</head>
<body>
  <main class="spread">
    <!-- back page -->
    <section class="page page-back">
      <header class="section-head">
        <p class="eyebrow">Featured Collection</p>
        <h2 class="section-title">Vanities, Faucets &amp; Surfaces</h2>
        <div class="section-rule"></div>
      </header>

      <div class="product-grid">
        <article class="product-card">
          <div class="product-photo photo-vanity" role="img" aria-label="Dark double-sink bathroom vanity with framed mirror"></div>
          <p class="product-category">Vanities</p>
          <h3 class="product-name">Espresso 72" Double</h3>
          <p class="product-desc">Solid-wood cabinet, white marble top, soft-close drawers.</p>
          <p class="product-price">From $649</p>
        </article>
        <article class="product-card">
          <div class="product-photo photo-faucet" role="img" aria-label="Chrome pull-down kitchen faucet"></div>
          <p class="product-category">Faucets</p>
          <h3 class="product-name">Arc Pull-Down</h3>
          <p class="product-desc">Brushed chrome, spring spout, ceramic cartridge.</p>
          <p class="product-price">From $119</p>
        </article>
        <article class="product-card">
          <div class="product-photo photo-surface" role="img" aria-label="Polished white marble surface tiles"></div>
          <p class="product-category">Surfaces</p>
          <h3 class="product-name">Carrara Marble</h3>
          <p class="product-desc">Polished 12 × 24 in. tile for floors and walls.</p>
          <p class="product-price">From $4.90 / sq ft</p>
        </article>
      </div>

      <section class="mail-panel" aria-label="Mailing panel">
        <div class="return-address">
          <div class="return-brand"><span class="brand-mark"></span><span class="return-name">Stonvale Depot</span></div>
          <p>2180 E. Calder Ave.</p>
          <p>Phoenix, AZ 85040</p>
        </div>
        <div class="indicia">PRSRT STD<br>U.S. POSTAGE<br>PAID<br>PHOENIX, AZ<br>PERMIT NO. 1827</div>
        <div class="addressee">
          <p class="addressee-code">****ECRWSS****</p>
          <p>Local Business Customer</p>
          <p>Phoenix, AZ 85040</p>
        </div>
        <div class="mail-teaser">Open inside for <strong>40–75% off</strong> retail</div>
      </section>
    </section>

    <!-- cover page -->
    <section class="page page-cover">
      <header class="masthead">
        <div class="masthead-brand"><span class="brand-mark"></span><span class="brand-name">Stonvale Depot</span></div>
        <p class="masthead-tag">Wholesale Hardware &amp; Building Supplies</p>
        <p class="masthead-area">Serving<br>Greater Phoenix</p>
      </header>

      <div class="hero" role="img" aria-label="Bright white kitchen with island, pendant lanterns and arched windows"></div>

      <div class="offer-badge">
        <p class="offer-lead">SAVE UP TO</p>
        <p class="offer-value">40–75% Off</p>
        <p class="offer-note">MAJOR RETAILER STORE PRICES</p>
      </div>

      <section class="range">
        <h2 class="range-title">Everything for Kitchen &amp; Bath</h2>
        <ul class="range-list">
          <li>Vanities</li><li>Faucets</li><li>Sinks</li>
          <li>Toilets</li><li>Bathtubs</li><li>Showers</li>
          <li>Tile</li><li>Range Hoods</li><li>Lighting</li>
          <li>Door Hardware</li><li>Mouldings</li><li>Kitchen Supply</li>
        </ul>
      </section>

      <section class="compare">
        <h2 class="compare-title">Compare Our Prices</h2>
        <table class="compare-table">
          <thead>
            <tr><th>Item</th><th class="num">Drent</th><th class="num ours">Stonvale Depot</th></tr>
          </thead>
          <tbody>
            <tr><td>72" Double Vanity</td><td class="num">$1,499</td><td class="num ours">$649</td></tr>
            <tr><td>Pull-Down Kitchen Faucet</td><td class="num">$329</td><td class="num ours">$119</td></tr>
            <tr><td>Porcelain Vessel Sink</td><td class="num">$249</td><td class="num ours">$89</td></tr>
          </tbody>
        </table>
      </section>

      <footer class="cover-footer">
        <span>2180 E. Calder Ave. Phoenix, AZ 85040</span>
        <strong>www.stonvaledepot-example.com</strong>
      </footer>
    </section>
  </main>
</body>
</html>
```